Berlins indisches Restaurant Nr. 1 sucht nach neue Visitenkarten
Zielgruppe
Wir sind Berlins führendes indisches Restaurant und Cocktailbar. Wir bieten leckere authentische Gerichte. Von Jugendlichen die gerne Cocktails trinken bis Firmen die bei uns große Events feiern ist alles dabei. Was bei uns hervorsticht ist die opulente Einrichtung. Sehr liebevoll ausgesucht und stimmig zusammengestellt. Fast alles Handarbeit von Manufakturen aus ganz Asien.
Nun suchen wir neue Visitenkarten. Das alte ist zu überladen. Es sollte wie wir 'anders' sein. Authentische exotische Küche aber dennoch modern. Viele Farben aber nicht zu kitschig. Übersichtlich aber dennoch viel Charme.
Gerne würden wir das Projekt -falls Designer uns zusagt- ausweiten. Logo, Flyer, Visitenkarten, Broschüren etc.
Bei der Größe der Visitenkarte sind wir flexibel. Es muss nicht die Standartgröße sein. Letztes mal war es eine Klappkarte. Gerne etwas neues.
Aufgabenstellung
Folgendes muss auf die Karte:
Adressen der 4 Standorte:
VELORA Kreuzberg – Lindholmer Weg 57 - 10999 Berlin - 030 487 319 6
VELORA Mitte – Kastelbrunner Allee 18 - 10117 Berlin - 030 5173 62 91
VELORA Schöneberg – Sommerhagstraße 33 - 10781 Berlin - 030 846 273 15
VELORA Hallgarter Platz – Quendelgasse 71 - 10117 Berlin - 030 739 516 04
Internetseite VELORA.de
evtl. verweis auf das TOSKAN Restaurant (2 mal in Berlin) mit Internetseite TOSKAN.de
Sätze die verwendet werden können:
Wer indisch mag, wird VELORA lieben...
Feel India in Berlin
A Culinary Tale of India in Berlin
Berlins Leading indian Restaurant (& Exotic Cocktailbar)

```html
<!DOCTYPE html>
<html lang="en">
<head>
<meta charset="utf-8">
<title>Berlins Leading Indian Restaurant</title>
<link rel="stylesheet" href="https://fonts.googleapis.com/css2?family=Bebas+Neue&display=swap">
<style>
  :root {
    --paper: #eeedeb;
    --paper-light: #f7f6f4;
    --saffron-deep: #e8821e;
    --saffron: #f0a623;
    --saffron-light: #f3c93a;
    --leaf-deep: #2f9c3a;
    --leaf: #4cb43a;
    --leaf-light: #7cc651;
    --ink: #0a0a0a;
  }
  html, body {
    margin: 0;
    padding: 0;
    overflow: hidden;
    background: var(--paper);
  }
  .card {
    position: relative;
    width: 1200px;
    height: 776px;
    overflow: hidden;
    background: radial-gradient(ellipse at 50% 50%, var(--paper-light) 0%, var(--paper) 75%);
  }
  .card__bands {
    position: absolute;
    inset: 0;
    width: 1200px;
    height: 776px;
  }
  .card__headline {
    position: absolute;
    left: 0;
    right: 0;
    top: 318px;
    margin: 0;
    text-align: center;
    font-family: "Bebas Neue", "Oswald", sans-serif;
    font-weight: 400;
    font-size: 60px;
    line-height: 88px;
    letter-spacing: 1.5px;
    color: var(--ink);
    text-transform: uppercase;
  }
  .card__headline span {
    display: block;
  }
</style>
</head>
<body>
<main class="card">
  <svg class="card__bands" viewBox="0 0 1200 776" xmlns="http://www.w3.org/2000/svg">
    <defs>
      <linearGradient id="saffron-wash" x1="0" y1="0" x2="1" y2="0">
        <stop offset="0" stop-color="var(--saffron-deep)"/>
        <stop offset="0.45" stop-color="var(--saffron)"/>
        <stop offset="1" stop-color="var(--saffron-light)"/>
      </linearGradient>
      <linearGradient id="leaf-wash" x1="0" y1="0" x2="1" y2="0">
        <stop offset="0" stop-color="var(--leaf-deep)"/>
        <stop offset="0.5" stop-color="var(--leaf)"/>
        <stop offset="0.85" stop-color="var(--leaf-light)"/>
        <stop offset="1" stop-color="var(--leaf-deep)"/>
      </linearGradient>
    </defs>
    <path class="band band--saffron" role="img" aria-label="Saffron watercolour band with a mandala ornament"
          fill="url(#saffron-wash)"
          d="M0 28 C120 18 260 8 420 12 C600 4 780 14 960 10 C1060 8 1140 14 1200 18
             L1200 288 C1120 280 1040 270 960 262 C860 250 760 226 660 214
             C560 204 440 200 330 214 C230 226 130 244 60 252 C36 255 16 258 0 260 Z"/>
    <path class="band band--leaf" role="img" aria-label="Green watercolour band with a mandala ornament"
          fill="url(#leaf-wash)"
          d="M0 568 C90 558 200 540 320 532 C440 522 560 530 680 534
             C800 538 920 540 1040 532 C1110 526 1160 512 1200 492
             L1200 776 L40 776 C28 740 16 700 0 670 Z"/>
  </svg>
  <h1 class="card__headline">
    <span>Berlins Leading Indian Restaurant</span>
    <span>(&amp; Exotic Cocktailbar)</span>
  </h1>
</main>
</body>
</html>
```